Book Cover needed for Printed Book entitled "Tango 7"

The Book's Title is "Tango 7", the sub-title is "A Neighbor's Manual for Quiet Evenings on the Block", and the author is "Desmond Farley". The front cover may have just the Title, or it may have a combination of the Title, Sub-Title, and Author. We would like to see designs that presents a feeling of peace and cooperation between US Police Officers and Civilians. The cover can include photographs, illustrations, or just words. But the cover should make the viewer want to open the book for more information.

Target Market(s)

Young adults who live in US inner-cities between ages 18 to 30.

Font styles to use
Sans Serif

Colors

Designer to choose colors to be used in the design.

Requirements
Must have
• Most US Police Officers use the phrase "TANGO 7" to tell other officers that the situation is under control and no assistance is needed. And the book will teach Civilians how to safely conduct themselves during police encounters - which will end with the Cops calling in "TANGO 7" to the dispatcher. So, the front cover must have the phrase "TANGO 7" in big bold letters.
Nice to have
• We would like to see designs that present a feeling of peace and cooperation between US Police Officers and Civilians. Pictures and illustrations of people are acceptable but is not required.

```html
<!DOCTYPE html>
<html lang="en">
<head>
<meta charset="utf-8">
<title>Tango 7 — Book Cover</title>
<link rel="stylesheet" href="https://fonts.googleapis.com/css2?family=Archivo+Black&family=Oswald:wght@300;600&display=swap">
<style>
  :root {
    --paper: #ffffff;
    --navy: #0a1f63;
    --signal-red: #b10a0a;
    --ink: #1c1c1c;
    --brass-light: #c9b06a;
    --brass-dark: #6d6a35;
    --ember: #e0773e;
  }
  html, body {
    margin: 0;
    padding: 0;
    overflow: hidden;
    background: var(--paper);
  }
  .cover {
    position: relative;
    width: 800px;
    height: 1200px;
    background: var(--paper);
    overflow: hidden;
  }
  .title {
    position: absolute;
    top: 38px;
    left: 0;
    width: 800px;
    margin: 0;
    text-align: center;
    font-family: "Archivo Black", "Arial Black", sans-serif;
    font-size: 168px;
    line-height: 1;
    letter-spacing: -6px;
    white-space: nowrap;
  }
  .title-word { color: var(--navy); }
  .title-number { color: var(--signal-red); margin-left: 34px; }
  .subtitle {
    position: absolute;
    top: 266px;
    left: 0;
    width: 800px;
    margin: 0;
    text-align: center;
    font-family: "Oswald", "Arial Narrow", sans-serif;
    font-weight: 300;
    font-size: 31px;
    letter-spacing: 0.2px;
    color: var(--ink);
    white-space: nowrap;
  }
  .emblem-art {
    position: absolute;
    top: 358px;
    left: 122px;
    width: 570px;
    height: 600px;
    border-radius: 18px 18px 48% 48% / 18px 18px 22% 22%;
    background: radial-gradient(ellipse at 50% 48%, var(--ember) 0%, #c8703c 28%, var(--brass-dark) 48%, var(--brass-light) 72%, #a8914d 100%);
    box-shadow: 0 22px 30px rgba(0,0,0,0.18);
  }
  .author {
    position: absolute;
    top: 1084px;
    left: 0;
    width: 800px;
    margin: 0;
    text-align: center;
    font-family: "Oswald", "Arial Narrow", sans-serif;
    font-weight: 600;
    font-size: 50px;
    letter-spacing: 6px;
    color: #111;
    white-space: nowrap;
  }
</style>
</head>
<body>
  <main class="cover">
    <h1 class="title"><span class="title-word">TANGO</span><span class="title-number">7</span></h1>
    <p class="subtitle">A Neighbor's Manual for Quiet Evenings on the Block</p>
    <div class="emblem-art" role="img" aria-label="Worn brass police badge with scales of justice engraved on an orange centre"></div>
    <p class="author">DESMOND FARLEY</p>
  </main>
</body>
</html>
```